Harbor Lantern Diagnostics
Stationary/Business Card
Project: Harbor Lantern Diagnostics
Harbor Lantern Diagnostics - Medical
Creative Brief
Use specific fonts
Font like in the uploaded pic (playing card)
Cutting-Edge
Marlo Quist
Chief Executive Officer
417 W Dunmore A Lubbock, Tx
marlo_047@quillpost.example
harborlanterndiagnostics.example
For the stationary I uploaded some ideas of how I would love for it to look like.
For the front and the back design of the business card, I have uploaded
orvell512 orvell512
I've already picked the winner for the logo but I'm still waiting on the finished product from the designer.

```html
<!DOCTYPE html>
<html lang="en">
<head>
<meta charset="utf-8">
<title>Harbor Lantern Diagnostics – Business Card</title>
<link href="https://fonts.googleapis.com/css2?family=Open+Sans:wght@400;600;700&display=swap" rel="stylesheet">
<style>
  :root {
    --backdrop: #d9d9d9;
    --card: #ffffff;
    --crimson: #8e1a1e;
    --crimson-deep: #6e1216;
    --gold: #e2a622;
    --gold-deep: #c98a12;
    --ink: #3a3a3a;
    --muted: #6b6b6b;
  }
  html, body {
    margin: 0;
    width: 1200px;
    height: 878px;
    overflow: hidden;
    background: var(--backdrop);
    font-family: "Open Sans", Arial, sans-serif;
  }
  .stage {
    width: 1200px;
    height: 878px;
    display: flex;
    align-items: center;
    justify-content: center;
    gap: 40px;
  }
  .card {
    position: relative;
    width: 540px;
    height: 309px;
    background: var(--card);
    box-shadow: 0 2px 6px rgba(0,0,0,0.12);
    overflow: hidden;
  }
  .brand {
    display: flex;
    align-items: center;
    gap: 8px;
  }
  .brand-dot {
    width: 10px;
    height: 10px;
    border-radius: 50%;
    background: var(--crimson);
    flex: none;
  }
  .brand-name {
    font-weight: 600;
    font-size: 12px;
    letter-spacing: 0.14em;
    text-transform: uppercase;
    color: var(--ink);
    white-space: nowrap;
  }
  .front .brand { position: absolute; left: 28px; top: 28px; }
  .contact {
    position: absolute;
    left: 300px;
    top: 108px;
  }
  .person-name {
    margin: 0;
    font-size: 17px;
    font-weight: 700;
    color: var(--crimson);
  }
  .person-title {
    margin: 1px 0 10px;
    font-size: 11px;
    color: var(--crimson);
  }
  .address {
    margin: 0 0 10px;
    font-size: 10.5px;
    line-height: 1.35;
    color: var(--muted);
  }
  .lines { list-style: none; margin: 0; padding: 0; }
  .lines li {
    display: flex;
    align-items: center;
    gap: 7px;
    font-size: 10.5px;
    line-height: 16px;
    color: var(--ink);
    white-space: nowrap;
  }
  .lines svg { width: 10px; height: 10px; fill: var(--crimson); flex: none; }
  .bands { position: absolute; left: 0; bottom: 0; width: 540px; height: 120px; }
  .website {
    position: absolute;
    left: 250px;
    bottom: 12px;
    font-size: 11px;
    letter-spacing: 0.03em;
    color: #ffffff;
    white-space: nowrap;
  }
  .back { display: flex; align-items: center; justify-content: center; }
  .back .brand-name { font-size: 15px; }
  .back .brand-dot { width: 13px; height: 13px; }
</style>
</head>
<body>
<main class="stage">
  <section class="card front" aria-label="Business card front">
    <div class="brand">
      <span class="brand-dot"></span>
      <span class="brand-name">Harbor Lantern Diagnostics</span>
    </div>

    <div class="contact">
      <h1 class="person-name">Marlo Quist</h1>
      <p class="person-title">Chief Executive Officer</p>
      <p class="address">417 W Dunmore A<br>Lubbock, Tx</p>
      <ul class="lines">
        <li><svg viewBox="0 0 10 10"><path d="M2 0.5h2l0.8 2.2-1.2 0.9a5 5 0 0 0 2.8 2.8l0.9-1.2 2.2 0.8v2a1 1 0 0 1-1 1A8.5 8.5 0 0 1 1 1.5a1 1 0 0 1 1-1z"/></svg>555 014 2290</li>
        <li><svg viewBox="0 0 10 10"><path d="M2.5 0.5h5v2.5h-5zM1 3.5h8v4H7.5v2h-5v-2H1zM3.5 6.5v2h3v-2z"/></svg>555 014 2291</li>
        <li><svg viewBox="0 0 10 10"><path d="M2.5 0h5a0.8 0.8 0 0 1 0.8 0.8v8.4a0.8 0.8 0 0 1-0.8 0.8h-5a0.8 0.8 0 0 1-0.8-0.8V0.8A0.8 0.8 0 0 1 2.5 0zM2.8 1.2v6.6h4.4V1.2z"/></svg>555 014 2292</li>
        <li><svg viewBox="0 0 10 10"><path d="M0.5 2h9v6h-9zM1.3 2.6 5 5.6l3.7-3z" fill-rule="evenodd"/></svg>marlo_047@quillpost.example</li>
      </ul>
    </div>

    <svg class="bands" viewBox="0 0 540 120" preserveAspectRatio="none" aria-hidden="true">
      <polygon points="0,66 215,66 228,80 0,80" fill="var(--crimson)"/>
      <polygon points="0,80 228,80 238,90 0,90" fill="var(--crimson-deep)"/>
      <polygon points="222,84 540,84 540,120 250,120" fill="var(--gold)"/>
      <polygon points="222,84 540,84 540,88 226,88" fill="var(--gold-deep)"/>
    </svg>
    <span class="website">www.harborlanterndiagnostics.example</span>
  </section>

  <section class="card back" aria-label="Business card back">
    <div class="brand">
      <span class="brand-dot"></span>
      <span class="brand-name">Harbor Lantern Diagnostics</span>
    </div>
  </section>
</main>
</body>
</html>
```